Cyber security firm needs to have a new look and modren website design

Vaultline Corp is already established and looking to improve the feel and UI of the site and cause potential clients to say "wow, let's contact them".
We provide cybersecurity assessment consulting services helping our clients to feel safer than they are now with a straightforward approach to data safety, as the current frameworks and regulations are NOT affective anymore.

the current site is: www.vaultline-example.biz

Please check the following sites:
norvekta-example.com
brimstalk-defense.example.com
https://www.quillmarsh-example.com

HomePage Design:
In general: we want to tell the viewer that it's a digital war out there, which is not a simple one. If not taking care of it will have causalities: https://www.quillmarsh-example.com/ see picture? See that and some what I'm afraid.... I need some assurance and safety...
1. Do not use the existing site content / design.
2. Do not use the 3 simple steps
3. Have slides top as it is now:
A Hacker Is Knocking, Are You READY? (and a matching picture)
4. Contact form on the right
5. 4 block services:
Web Application Security.
Internal / External Vulnerability Assessments.
Penetration Testing.
Malware Attack Simulation.
6. Recent News: 3 Blocks
7. Recent Posts: 3 Blocks
8. Under the contact form: Download out FREE Report Cybersecurity Assessment Framework
9. Top contact form search line.
10. Bottom page should show all links from top menu
11. This design should work on WordPress

Thanks.

Target Market(s)

Right now: Financials.
Looking to have to add more, will decide later.

Industry/Entity Type

Security

Coding

Coded - Design and coding required

Number of Pages Required

5+ page

Font styles to use
Other font styles liked:
• Caliberi

Requirements
Must have
• Our site is based on CMS: WordPress
• Should be progressive: to be showed on any device: PC, tablets and phones.
• Browsers: IE, Chrome and Firefox.
• Look serious, experts in their field and getting tasks done!
• Use the same fonts from:
• norvekta-example.com
• brimstalk-defense.example.com
• https://www.quillmarsh-example.com

```html
<!DOCTYPE html>
<html lang="en">
<head>
<meta charset="utf-8">
<title>Vaultline Corp — Cybersecurity Assessment Consulting</title>
<link href="https://fonts.googleapis.com/css2?family=Carlito:ital,wght@0,400;0,700;1,400&display=swap" rel="stylesheet">
<style>
:root{
  --navy:#1d3d6e;
  --sky:#2f74c0;
  --ink:#222;
  --muted:#555;
  --nav:#3b3b3b;
  --hero:#000;
  --red:#a5192b;
  --red-dark:#7f0f1e;
  --badge:#e2762b;
  --panel:#5c5c5c;
  --panel-dark:#4a4a4a;
  --white:#fff;
  --field-border:#8a8a8a;
}
*{box-sizing:border-box;margin:0;padding:0}
html,body{width:1200px;height:2526px;overflow:hidden;background:var(--white)}
body{font-family:"Carlito",Calibri,Arial,sans-serif;color:var(--ink);position:relative}
.abs{position:absolute}

/* header */
.brand{left:100px;top:40px}
.brand-name{font-size:62px;font-weight:700;color:var(--navy);line-height:1;letter-spacing:1px}
.brand-tag{font-size:20px;color:var(--sky);margin-top:4px;margin-left:60px}
.phone{right:46px;top:84px;font-size:30px;font-style:italic;font-weight:700;color:#333}

/* nav */
.top-nav{left:0;top:158px;width:1200px;height:57px;background:var(--nav)}
.menu{position:absolute;left:72px;top:13px;color:var(--white);font-size:30px;display:flex;gap:0}
.menu span{padding:0 18px}
.menu .sep{padding:0}
.search{position:absolute;left:783px;top:10px;width:392px;height:38px;background:var(--white);border:1px solid #999}
.search svg{position:absolute;right:4px;top:3px}

/* hero */
.hero{left:0;top:215px;width:1200px;height:600px;background:var(--hero);overflow:hidden}
.hero-photo{position:absolute;left:630px;top:0;width:570px;height:600px;background:radial-gradient(ellipse at 55% 45%,#9a9a9a 0%,#5a5a5a 30%,#2a2a2a 60%,#000 100%)}
.hero-title{position:absolute;left:90px;top:100px;font-size:56px;color:var(--white)}
.hero-ask{position:absolute;left:200px;top:230px;font-size:66px;color:var(--white)}
.hero-ready{position:absolute;left:250px;top:300px;font-size:118px;color:var(--white);letter-spacing:2px}
.seal{position:absolute;left:65px;top:445px;width:108px;height:108px;border-radius:50%;background:var(--sky);border:5px solid #cfe0f4}
.quote{position:absolute;left:212px;top:460px;width:470px;font-size:19px;font-style:italic;color:var(--white);line-height:1.3}

/* services */
.services{left:0;top:815px;width:1200px;height:295px;background:var(--red);border-bottom:6px solid var(--red-dark)}
.service{position:absolute;top:0;width:300px;text-align:center;color:var(--white)}
.service .mark{width:98px;height:98px;margin:42px auto 0;border-radius:50%;background:var(--badge);border:6px solid #f4d2b4}
.service .label{font-size:29px;line-height:1.15;margin-top:30px}

/* contact form */
.contact{left:63px;top:1140px;width:400px}
.field{position:absolute;left:0;font-size:19px}
.field input,.field select,.field textarea{display:block;width:400px;height:38px;margin-top:8px;border:1px solid var(--field-border);background:var(--white)}
.field select{width:190px;height:26px}
.field textarea{height:62px}
.opt-in{position:absolute;left:20px;top:413px;font-size:19px;display:flex;gap:12px;line-height:1.2}
.opt-in i{display:block;width:20px;height:20px;border:1px solid var(--field-border);flex:none;margin-top:2px}
.send{position:absolute;left:0;top:755px;width:162px;height:60px;border-radius:6px;background:linear-gradient(var(--red),var(--red-dark));color:var(--white);font-size:28px;text-align:center;line-height:60px}

.report{left:54px;top:2005px;width:390px;height:430px;border-radius:26px;background:linear-gradient(160deg,#3f8fe0,#1c57a8);color:var(--white);text-align:center;padding-top:66px}
.report .lead{font-size:40px;line-height:1.15}
.report .big{font-size:50px;line-height:1.12;margin-top:4px}

/* main */
.intro{left:500px;top:1130px;width:680px}
.intro .lede{font-size:26px;line-height:1.35;color:var(--ink)}
.intro .body{font-size:16px;line-height:1.9;color:var(--ink);margin-top:22px}
.intro ul{list-style:none;margin-left:90px}
.intro li::before{content:"• "}

.section-title{font-size:30px;color:var(--ink)}
.tiles{width:675px;height:326px;background:var(--panel);border-bottom:60px solid var(--panel-dark)}
.tile{position:absolute;top:12px;height:198px;width:200px}
.t1{background:linear-gradient(135deg,#cfe0ee,#6f8fa8)}
.t2{background:linear-gradient(135deg,#c79a3a,#3b2a12)}
.t3{background:linear-gradient(135deg,#d8d8d8,#5b5b5b)}
.t4{background:linear-gradient(135deg,#c9d0d6,#7a858f)}
.t5{background:linear-gradient(135deg,#d9c9c4,#6a1e22)}
.t6{background:linear-gradient(135deg,#eae6df,#3d3a36)}

/* footer */
.footer{left:0;top:2478px;width:1200px;height:48px;background:var(--nav);color:var(--white);font-size:27px;text-align:center;line-height:48px}
.footer span{padding:0 16px}
</style>
</head>
<body>

<header>
  <div class="abs brand">
    <div class="brand-name">Vaultline Corp</div>
    <div class="brand-tag">safeguarding your data</div>
  </div>
  <div class="abs phone">1-555-014-2270</div>
</header>

<nav class="abs top-nav">
  <div class="menu"><span>Home</span><span class="sep">|</span><span>Why Us?</span><span class="sep">|</span><span>Services</span><span class="sep">|</span><span>About</span><span class="sep">|</span><span>Media</span></div>
  <div class="search">
    <svg width="32" height="32" viewBox="0 0 32 32"><rect width="32" height="32" fill="#e6e6e6" stroke="#999"/><circle cx="14" cy="13" r="7" fill="none" stroke="#555" stroke-width="2.5"/><line x1="19" y1="18" x2="26" y2="25" stroke="#555" stroke-width="3"/></svg>
  </div>
</nav>

<section class="abs hero">
  <div class="hero-photo" role="img" aria-label="Close-up photo of a metal door knocker on a dark door"></div>
  <div class="hero-title">A Hacker is Knocking</div>
  <div class="hero-ask">Are You</div>
  <div class="hero-ready">READY?</div>
  <div class="seal"></div>
  <p class="quote">“Cybersecurity consultant Vaultline has developed a product tailored to the needs of hedge fund managers.” - Oct. 30, 2013 www.fundwatch-example.com</p>
</section>

<section class="abs services">
  <div class="service" style="left:24px"><div class="mark"></div><div class="label">Web Application<br>Security</div></div>
  <div class="service" style="left:299px"><div class="mark"></div><div class="label">Internal / External<br>Vulnerability<br>Assessments</div></div>
  <div class="service" style="left:592px"><div class="mark"></div><div class="label">Penetration<br>Testing</div></div>
  <div class="service" style="left:876px"><div class="mark"></div><div class="label">Malware Attack<br>Simulation</div></div>
</section>

<form class="abs contact">
  <label class="field" style="top:8px">Your Name *<input type="text"></label>
  <label class="field" style="top:92px">Your Name*<input type="text"></label>
  <label class="field" style="top:170px">Company Name<input type="text"></label>
  <label class="field" style="top:250px">Phone<input type="text"></label>
  <label class="field" style="top:328px">Interested In:<select><option>-----</option></select></label>
  <div class="opt-in"><i></i><span>Please send me Cybersecurity Educational<br>Updates</span></div>
  <label class="field" style="top:485px">Subject *<input type="text"></label>
  <label class="field" style="top:565px">Message<textarea></textarea></label>
  <label class="field" style="top:675px">How did you find Vaultline?<select><option>-----</option></select></label>
  <div class="send">Send</div>
</form>

<aside class="abs report">
  <div class="lead">Download<br>our FREE Report</div>
  <div class="big">Cybersecurity<br>Assessment<br>Framework</div>
</aside>

<section class="abs intro">
  <p class="lede">Are you searching online for a CyberSecurity firm because your company network was breached? Or, do you want to prevent future breaches? We can help you.</p>
  <div class="body">
    <p>If you are a hedge fund or an investment firm’s CTO/CISO/ISO or an IT manager with 100 or more computer users, who are frustrated with the level of service, responsiveness and competence of your current security consulting provider, and if you’re TIRED of dealing with ongoing security incidents, then we can help your organization by:</p>
    <p>• Hacking your network &amp; systems, in order to identify potential breaches BEFORE they accrue</p>
    <ul>
      <li>Sweeping your network devices for an existing weakness</li>
      <li>Providing you with a comprehensive CyberSecurity Risk Analysis</li>
      <li>Being proactive by taking ownership of the process</li>
    </ul>
  </div>
</section>

<section class="abs" style="left:500px;top:1678px">
  <h2 class="section-title" style="font-weight:400">Recent News</h2>
  <div class="tiles" style="position:relative;margin-top:6px">
    <div class="tile t1" style="left:15px" role="img" aria-label="Photo of a person working at a computer"></div>
    <div class="tile t2" style="left:238px" role="img" aria-label="Photo of golden keyboard keys"></div>
    <div class="tile t3" style="left:462px" role="img" aria-label="Photo of a USB security key"></div>
  </div>
</section>

<section class="abs" style="left:500px;top:2064px">
  <h2 class="section-title" style="font-weight:400">Recent Posts</h2>
  <div class="tiles" style="position:relative;margin-top:6px;height:320px">
    <div class="tile t4" style="left:15px" role="img" aria-label="Photo of a computer mouse and keyboard"></div>
    <div class="tile t5" style="left:238px" role="img" aria-label="Photo of a chained and locked door handle"></div>
    <div class="tile t6" style="left:462px" role="img" aria-label="Photo of a person at a desk with monitors"></div>
  </div>
</section>

<footer class="abs footer">
  <span>Home</span>|<span>Why Us?</span>|<span>Services</span>|<span>About</span>|<span>Media</span>
</footer>

</body>
</html>
```